Wound Care Flyer

Looking for a Trifold brochure that is modern and has a high aesthetic. (Specialty services) Would like the colors to center around Black and Gold. Possibly updating the logo. Attached is the old brochure and a document about our services.

```html
<!DOCTYPE html>
<html lang="en">
<head>
<meta charset="utf-8">
<title>Cedarline Wounds – Trifold Brochure</title>
<link rel="stylesheet" href="https://fonts.googleapis.com/css2?family=Montserrat:wght@400;500;600;700;800&family=Poppins:wght@400;500;600&display=swap">
<style>
:root{
  --black:#0d0d0d;
  --black-soft:#1c1c1c;
  --gold:#b8935a;
  --gold-light:#d9b57a;
  --gold-dark:#8a6a3a;
  --gold-panel:linear-gradient(160deg,#8d6c3e 0%,#b8935a 45%,#c9a772 100%);
  --white:#ffffff;
  --ink:#161616;
  --page:#b9b9b9;
}
*{box-sizing:border-box;margin:0;padding:0}
html,body{width:1200px;height:2617px;overflow:hidden}
body{background:var(--page);font-family:"Montserrat",sans-serif;color:var(--white);position:relative}
.spread{position:absolute;left:153px;width:912px;height:705px;background:var(--black);overflow:hidden}
.spread-outer{top:581px}
.spread-inner{top:1331px}
.abs{position:absolute}
.wave{position:absolute;left:0;top:0;width:912px;height:705px}
.heading{font-family:"Montserrat",sans-serif;font-weight:800;color:var(--gold);letter-spacing:.2px}
.body-copy{font-family:"Montserrat",sans-serif;font-size:12.3px;line-height:13.6px;color:var(--white)}
.photo{position:absolute;border-radius:50%;border:4px solid var(--black);box-shadow:0 0 0 5px var(--gold),0 0 0 8px var(--black)}
.brand{display:flex;align-items:center;gap:8px;font-family:"Montserrat",sans-serif;font-weight:600;font-size:13px;letter-spacing:2px;color:var(--gold-light);text-transform:uppercase}
.brand-dot{width:12px;height:12px;border-radius:50%;background:var(--gold-light)}
/* outer spread */
.about-title{left:40px;top:28px;font-size:24px}
.about-copy{left:40px;width:245px}
.serving{left:38px;top:566px;font-size:11.5px;color:var(--gold-light)}
.places{left:38px;top:584px;display:grid;grid-template-columns:86px 130px;row-gap:4px;font-size:12.5px}
.place{display:flex;align-items:center;gap:4px}
.place svg{width:7px;height:10px}
.tagline{left:304px;width:306px;top:396px;text-align:center;font-family:"Montserrat",sans-serif;font-weight:600;font-size:17px}
.contact{left:304px;width:306px;text-align:center;font-size:12px}
.contact-icon{display:block;width:20px;height:20px;margin:0 auto 4px;border-radius:50%;border:1.5px solid var(--gold);position:relative}
.contact-icon::after{content:"";position:absolute;left:5px;top:5px;width:7px;height:7px;border-radius:50%;background:var(--gold)}
.badge{left:647px;top:152px;width:200px;height:200px;border-radius:50%;background:radial-gradient(circle at 50% 40%,#2a2a2a,#0b0b0b);box-shadow:0 0 0 6px var(--gold),0 0 0 10px var(--black),0 0 0 12px var(--gold-dark);text-align:center;font-family:"Montserrat",sans-serif;font-weight:800;line-height:27px;padding-top:48px}
.badge .l1{font-size:21px;color:var(--white)}
.badge .l2{font-size:29px;color:var(--gold)}
.portrait{left:690px;top:300px;width:118px;height:270px;border-radius:50px 50px 10px 10px;background:linear-gradient(180deg,#5a3c2c 0%,#f2f2f2 25%,#e7e5ea 60%,#c9a8bc 100%)}
.name-arc{left:612px;top:570px;width:270px;height:270px;border-radius:50%;background:var(--gold-panel);box-shadow:0 0 0 4px var(--black),0 0 0 6px var(--gold)}
.name{left:612px;width:270px;top:603px;text-align:center;font-family:"Poppins",sans-serif;font-weight:600;font-size:20px;line-height:22px}
.name small{display:block;font-size:14px;font-weight:500}
/* inner spread */
.inner-left{left:0;top:0;width:597px;height:705px;background:linear-gradient(180deg,#1d1d1d,#0a0a0a)}
.inner-right{left:597px;top:0;width:315px;height:705px;background:var(--gold-panel)}
.brand-title{left:40px;top:30px;font-size:24px}
.pill{display:inline-block;background:var(--gold);color:var(--white);font-size:13px;line-height:14px;padding:7px 13px;border-radius:14px;font-family:"Montserrat",sans-serif;font-weight:500}
.col-a{left:40px;top:78px;width:225px}
.col-b{left:338px;top:78px;width:225px}
.col-a .body-copy,.col-b .body-copy{font-size:10.8px;line-height:11.7px;margin-top:8px}
.sub{font-family:"Montserrat",sans-serif;font-weight:700;font-size:11.5px;color:var(--gold);margin-top:9px}
.sub.plain{font-weight:500}
.list{list-style:none;margin-top:6px}
.list li{display:flex;align-items:center;gap:6px;border:1.2px solid var(--gold);border-radius:3px;padding:2px 6px;font-size:10.5px;line-height:10.5px;margin-bottom:5px;min-height:24px}
.list.tight li{min-height:19px;margin-bottom:4px;padding:2px 6px}
.li-icon{flex:none;width:11px;height:11px;border-radius:2px;background:var(--gold)}
.right-copy{left:637px;width:245px;color:var(--white)}
.right-copy.title{top:30px;font-family:"Montserrat",sans-serif;font-weight:800;font-size:24px;line-height:26px;color:var(--ink)}
.right-copy .body-copy{font-size:10.8px;line-height:11.7px}
.partner-title{left:637px;top:243px;font-family:"Montserrat",sans-serif;font-weight:700;font-size:13px;color:var(--ink)}
.benefit{left:637px;width:262px}
.benefit-head{display:flex;align-items:center;gap:8px}
.benefit-icon{flex:none;width:22px;height:22px;border-radius:50%;background:var(--black);box-shadow:0 0 0 2px var(--white);position:relative}
.benefit-icon::after{content:"";position:absolute;left:7px;top:7px;width:8px;height:8px;border-radius:50%;border:1.5px solid var(--white)}
.benefit-pill{background:var(--gold-light);color:var(--ink);font-weight:700;font-size:11.5px;padding:3px 8px;border-radius:10px}
.benefit p{margin-left:30px;margin-top:7px;font-size:10.5px;line-height:11.4px}
</style>
</head>
<body>

<section class="spread spread-outer" aria-label="Brochure outer spread">
  <svg class="wave" viewBox="0 0 912 705" aria-hidden="true">
    <defs>
      <linearGradient id="goldFill" x1="0" y1="0" x2="1" y2="1">
        <stop offset="0" stop-color="#8d6c3e"/><stop offset=".5" stop-color="#b8935a"/><stop offset="1" stop-color="#c9a772"/>
      </linearGradient>
    </defs>
    <rect x="0" y="0" width="304" height="705" fill="#181818"/>
    <path d="M304,0 H610 V400 C520,415 440,468 304,476 Z" fill="url(#goldFill)"/>
    <path d="M0,385 C110,455 210,482 304,476 C440,468 520,415 610,400 C720,382 820,378 912,372" fill="none" stroke="#c9a772" stroke-width="5"/>
    <path d="M0,398 C110,468 210,494 304,488 C440,480 520,427 610,412 C720,394 820,390 912,384" fill="none" stroke="#0b0b0b" stroke-width="10"/>
  </svg>

  <h2 class="abs heading about-title">About Us</h2>
  <p class="abs body-copy about-copy" style="top:74px">We provide an additional layer of expertise by utilizing advanced the advanced technology of biological skin substitute grafts.</p>
  <p class="abs body-copy about-copy" style="top:155px">We pride ourselves in working in close coordination with the patient's care team, including home health services and the primary care physician (PCP).</p>
  <p class="abs body-copy about-copy" style="top:237px">Weensure seamless integration without duplicating services prioritizing collaborative care, sharing detailed notes and working closely with the patient's home health team on days between visits.</p>

  <div class="photo" role="img" aria-label="Photo of a bandaged foot resting on a clinic bed" style="left:40px;top:338px;width:190px;height:190px;background:radial-gradient(circle at 45% 40%,#f4f4f4,#c9d3dc 55%,#6e8aa6)"></div>

  <p class="abs serving">Serving the greater North Houston area.</p>
  <div class="abs places">
    <span class="place"><svg viewBox="0 0 7 10"><path d="M3.5 0a3.5 3.5 0 0 1 3.5 3.5C7 6 3.5 10 3.5 10S0 6 0 3.5A3.5 3.5 0 0 1 3.5 0z" fill="#d9b57a"/></svg>Spring</span>
    <span class="place"><svg viewBox="0 0 7 10"><path d="M3.5 0a3.5 3.5 0 0 1 3.5 3.5C7 6 3.5 10 3.5 10S0 6 0 3.5A3.5 3.5 0 0 1 3.5 0z" fill="#d9b57a"/></svg>The Woodlands</span>
    <span class="place"><svg viewBox="0 0 7 10"><path d="M3.5 0a3.5 3.5 0 0 1 3.5 3.5C7 6 3.5 10 3.5 10S0 6 0 3.5A3.5 3.5 0 0 1 3.5 0z" fill="#d9b57a"/></svg>Willis</span>
    <span class="place"><svg viewBox="0 0 7 10"><path d="M3.5 0a3.5 3.5 0 0 1 3.5 3.5C7 6 3.5 10 3.5 10S0 6 0 3.5A3.5 3.5 0 0 1 3.5 0z" fill="#d9b57a"/></svg>Montgomery</span>
    <span class="place"><svg viewBox="0 0 7 10"><path d="M3.5 0a3.5 3.5 0 0 1 3.5 3.5C7 6 3.5 10 3.5 10S0 6 0 3.5A3.5 3.5 0 0 1 3.5 0z" fill="#d9b57a"/></svg>Tomball</span>
    <span class="place"><svg viewBox="0 0 7 10"><path d="M3.5 0a3.5 3.5 0 0 1 3.5 3.5C7 6 3.5 10 3.5 10S0 6 0 3.5A3.5 3.5 0 0 1 3.5 0z" fill="#d9b57a"/></svg>Conroe</span>
    <span class="place"><svg viewBox="0 0 7 10"><path d="M3.5 0a3.5 3.5 0 0 1 3.5 3.5C7 6 3.5 10 3.5 10S0 6 0 3.5A3.5 3.5 0 0 1 3.5 0z" fill="#d9b57a"/></svg>Magnolia</span>
    <span class="place"><svg viewBox="0 0 7 10"><path d="M3.5 0a3.5 3.5 0 0 1 3.5 3.5C7 6 3.5 10 3.5 10S0 6 0 3.5A3.5 3.5 0 0 1 3.5 0z" fill="#d9b57a"/></svg>Cypress</span>
  </div>

  <div class="photo" role="img" aria-label="Photo of gloved hands dressing a patient's wound" style="left:345px;top:30px;width:222px;height:222px;background:radial-gradient(circle at 50% 45%,#e9eef2,#b9c6d2 50%,#5d7892)"></div>
  <div class="abs brand" style="left:304px;width:306px;top:330px;justify-content:center;color:var(--white)"><span class="brand-dot" style="background:var(--white)"></span>Cedarline Wounds</div>
  <p class="abs tagline">getting in touch with us</p>

  <p class="abs contact" style="top:488px"><span class="contact-icon"></span>(555) 014-2280</p>
  <p class="abs contact" style="top:535px"><span class="contact-icon"></span>(555) 014-7319</p>
  <p class="abs contact" style="top:578px"><span class="contact-icon"></span>hello@cedarlinewounds.com</p>
  <p class="abs contact" style="top:617px"><span class="contact-icon"></span>www.cedarlinewounds.com</p>

  <div class="abs brand" style="left:610px;width:302px;top:70px;justify-content:center"><span class="brand-dot"></span>Cedarline Wounds</div>
  <div class="abs badge"><div class="l1">ADVANCED</div><div class="l2">WOUND</div><div class="l2">CARE</div></div>
  <div class="abs portrait" role="img" aria-label="Portrait of the nurse practitioner in a white coat"></div>
  <div class="abs name-arc"></div>
  <p class="abs name">Dana Merritt<small>FNP-C</small></p>
</section>

<section class="spread spread-inner" aria-label="Brochure inner spread">
  <div class="abs inner-left"></div>
  <div class="abs inner-right"></div>

  <h2 class="abs heading brand-title">Cedarline Wounds:</h2>

  <div class="abs col-a">
    <span class="pill" style="width:180px">Mobile Wound Care</span>
    <p class="body-copy">With a focus on convenience, expertise, and compassion, we bring the highest standard of wound care directly to the patient's home. Working side-by-side with the patient's physician, our team of experienced specialists utilize cutting-edge technology and personalized treatment plans to ensure optimal healing and comfort. From thorough wound assessments to advanced therapies and ongoing support, we prioritize the well-being of our patients every step of the way.</p>
    <p class="sub plain">Whether it's managing</p>
    <ul class="list">
      <li><span class="li-icon"></span>Chronic wounds</li>
      <li><span class="li-icon"></span>Post-surgery recovery</li>
      <li><span class="li-icon"></span>We go above beyond to Provide comprehensive</li>
      <li><span class="li-icon"></span>Compassionate care</li>
    </ul>
    <p class="body-copy" style="margin-top:10px">With our concierge approach, we aim to make the healing journey as seamless and comfortable as possible, empowering our patients to live their best lives.</p>
  </div>

  <div class="abs col-b">
    <span class="pill" style="line-height:13px;padding:4px 13px">Leaders in Mobile<br>Advanced Wound Care.</span>
    <p class="body-copy">We provide a complete wound management program for our patients that includes the use of advanced treatments, the creation of care plans, and coordination of care with other clinicians. Our comprehensive in-home wound care services include:</p>
    <p class="sub">Advanced Wound Assessment</p>
    <p class="body-copy" style="margin-top:2px">Thorough evaluation of <b>wound type, size, and stage</b> to develop a tailored treatment plan.</p>
    <p class="sub">Cutting-Edge Treatments</p>
    <p class="body-copy" style="margin-top:2px">Utilization of the latest technologies and techniques in wound care, including:</p>
    <ul class="list tight">
      <li><span class="li-icon"></span>Compression</li>
      <li><span class="li-icon"></span>Biologic Skin Substitutes</li>
      <li><span class="li-icon"></span>Negative Pressure Wound Therapy</li>
      <li><span class="li-icon"></span>Collagen and Advanced Dressings</li>
      <li><span class="li-icon"></span>Surgical/ Trauma Wounds</li>
      <li><span class="li-icon"></span>Venous/ Arterial Wounds</li>
      <li><span class="li-icon"></span>Debridements</li>
    </ul>
  </div>

  <svg class="wave" viewBox="0 0 912 705" aria-hidden="true">
    <path d="M0,585 C150,515 300,535 470,587 C620,633 760,635 912,595 V705 H0 Z" fill="#0b0b0b"/>
    <path d="M0,587 C150,517 300,537 470,589 C620,635 760,637 912,597" fill="none" stroke="#c9a772" stroke-width="4"/>
  </svg>

  <div class="photo" role="img" aria-label="Photo of a clinician treating a leg wound" style="left:60px;top:505px;width:165px;height:165px;background:radial-gradient(circle at 45% 50%,#d8a47a,#6f94b8 60%,#37587a)"></div>
  <div class="photo" role="img" aria-label="Photo of sterile wound care instruments and supplies" style="left:342px;top:515px;width:160px;height:160px;background:radial-gradient(circle at 50% 45%,#eef0f2,#a8b2bc 55%,#5b6470)"></div>

  <h2 class="abs right-copy title">Personalized<br>Care Plans</h2>
  <div class="abs right-copy" style="top:100px">
    <p class="body-copy">Customized care plans designed to meet the specific needs of each patient, ensuring optimal healing. Coordination and direction of care for other caregivers and clinicians, including home health.</p>
    <p class="body-copy" style="margin-top:12px">Patient and Caregiver Education Providing education and support to patients and their caregivers to enhance understanding and promote self-care.</p>
  </div>
  <p class="abs partner-title">Partner with Cedarline Wounds:</p>

  <div class="abs benefit" style="top:275px">
    <div class="benefit-head"><span class="benefit-icon"></span><span class="benefit-pill">Enhanced Patient Outcomes</span></div>
    <p>Our specialized expertise in advanced wound care leads to faster healing times and improved patient satisfaction</p>
  </div>
  <div class="abs benefit" style="top:358px">
    <div class="benefit-head"><span class="benefit-icon"></span><span class="benefit-pill">Extended Reach</span></div>
    <p>Our in-home services allow your patients to receive high-quality care without the need for frequent visits, reducing the burden on your resources.</p>
  </div>
  <div class="abs benefit" style="top:450px">
    <div class="benefit-head"><span class="benefit-icon"></span><span class="benefit-pill">Professional Integrity</span></div>
    <p>As a trusted partner, we uphold the highest standards of care and professionalism, reflecting positively on your clinic's reputation.</p>
  </div>
  <div class="abs benefit" style="top:542px">
    <div class="benefit-head"><span class="benefit-icon"></span><span class="benefit-pill">Seamless Collaboration</span></div>
    <p>We maintain open communication with referring clinics, ensuring a coordinated approachto patient care</p>
  </div>
</section>

</body>
</html>
```